Web re-design project for web software development agency

We need to re-design our existing website (www.tovenmedia.co.uk), and are going to start using a shorter domain (www.toven.com).
We have been in business for 8 years and it's time for an update.

We are based at Harrowmede Court (home of the code breakers). We specialise in writing software for the web. Over the years we have built up a healthy customer base and it is time to incorporate the features we build for our customers into our own site (e.g. social media).

We have a team of 8 talented developers with varied skills including: apps for mobile; complex server side software; front-end software; eCommerce software; specialised web based applications; integration software; hardware support; consultancy services. Our customers are diverse (e.g. banking; commerce; veterinary; R&D; health sector; law; accounting; film industry etc.).

Our current colour scheme is blue, white and green although we are not averse to moving away from these colours. We will also be dropping the DESIGN from our name and logo. Revised logo will be attached.

The site needs to be modern, sophisticated and leading edge. We want to show visitors to the site that we are a professional organisation.
Updates

Our logo in PSD format has been uploaded. Please drop the word DESIGN from the logo.

The deliverable for this project is a PSD (ideally we would like to see how the home page, portfolio page, resources page with mugshots, and forms are going to look).

Many thanks,
Tom

Please DO NOT include a Careers section 

We will also need a "meet our team" section with spaces for 10 photographs as well as some space underneath them so that we can add a short paragraph for each one of them.

Target Market(s)

Mainly large corporations needing bespoke web software, or generally complex projects (for anyone).

Industry/Entity Type

Software

Requirements
Must have
• We would like a home page designed that has the following elements on it:
- Show the new cookie compliance policy displayed probably in the top of the page (will disappear).
- A client Testimonial.
- Pricing icon.
- Social media Links.
- A Quote section in expand/collapse field as in (http://www.quillbrook-online.co.uk/our-services.shtml)

We would also like a portfolio page that showcases our clients in an interesting way.

Finally, we would like a form design that we can use throughout the site (i.e. how should buttons, radio buttons, checkboxes, dropdowns, text areas etc. look)?
Nice to have
• A page that follows these guidelines:
http://www.pagerivet.com/the-anatomy-of-a-perfect-landing-page

Here are a few examples of sites in our sector that we like:
- http://www.tidewell-studio.com/
- http://plinthos.co.uk/
- http://www.fernaxis.com/services/web-development (nice contact us page)
- http://www.quillbrook-online.co.uk/
- http://www.lumsa.com/
- http://www.netmoxa.co.uk/
Should not have
• No flash elemets. If anything, we will use html5.

```html
<!DOCTYPE html>
<html lang="en">
<head>
<meta charset="utf-8">
<title>Toven — Web Application Development and Support</title>
<link href="https://fonts.googleapis.com/css2?family=Exo+2:ital,wght@0,200;0,300;0,400;0,500;0,600;1,300&display=swap" rel="stylesheet">
<style>
:root{
  --bg:#0c4271;
  --navy:#0b2744;
  --lime:#c9d63b;
  --white:#ffffff;
  --ink:#555c63;
  --ink-dark:#3d4449;
  --heading:#123e6a;
  --line:#1e5488;
}
*{box-sizing:border-box;margin:0;padding:0}
html,body{width:1200px;height:1161px;overflow:hidden}
body{position:relative;background:linear-gradient(#0a3963 0,var(--bg) 200px,var(--bg) 1100px);font-family:"Exo 2",sans-serif;color:var(--white)}
.abs{position:absolute}

.logo{left:120px;top:30px;display:flex;align-items:center;gap:6px;font-weight:600;font-size:21px;letter-spacing:.5px}
.logo-mark{width:20px;height:20px;background:var(--lime)}
.nav{left:479px;top:20px;display:flex;height:50px;align-items:center;font-size:14px;color:var(--lime)}
.nav a{color:inherit;text-decoration:none;margin-right:29px}
.nav .current{background:var(--navy);color:var(--white);font-weight:600;height:50px;width:71px;display:flex;align-items:center;justify-content:center;margin-right:15px;position:relative}
.corner{position:absolute;width:10px;height:10px;border-color:var(--lime);border-style:solid}
.c-tr{top:0;right:0;border-width:2px 2px 0 0}
.c-bl{bottom:0;left:0;border-width:0 0 2px 2px}
.rule{height:1px;background:var(--line)}

.headline{left:118px;top:98px;font-weight:200;font-size:46px;letter-spacing:-1.5px;white-space:nowrap}
.headline span{color:var(--lime)}

.hero{left:80px;top:170px;width:1040px;height:240px;background:var(--white)}
.code-art{position:absolute;left:500px;top:0;width:320px;height:240px;background:linear-gradient(100deg,#fff 0,#eef1f4 40%,#e6eaee 70%,#fff 100%)}
.hero h2{position:absolute;left:40px;top:40px;color:var(--heading);font-weight:500;font-size:20px;line-height:24px;z-index:1}
.benefits{position:absolute;left:40px;top:112px;list-style:none;font-size:13.5px;color:var(--ink);line-height:22px;z-index:1;white-space:nowrap}
.benefits svg{vertical-align:-1px;margin-right:7px}
.benefits b{font-weight:600;color:var(--ink-dark)}
.pricing{position:absolute;left:573px;top:115px;width:147px;height:83px;background:linear-gradient(#d3df48,#bfcc30);display:flex;flex-direction:column;align-items:center;justify-content:flex-end;padding-bottom:12px;font-size:19px;font-weight:500;box-shadow:0 3px 8px rgba(0,0,0,.25);z-index:2}
.monitor{left:795px;top:188px;width:285px;height:250px;border-radius:8px;background:linear-gradient(#2b2b2d 0,#1b1b1c 69%,#c9cbcd 69%,#e5e6e7 80%,transparent 80%)}

.quote-panel{left:80px;top:410px;width:1040px;height:270px;background:linear-gradient(#e9e9ea,#f3f3f3 40%,#c9c9cb)}
.quote-panel p{position:absolute;left:39px;top:19px;font-size:13.5px;color:var(--navy)}
.quote-panel b{font-weight:600}
.field{position:absolute;width:230px;height:40px;background:linear-gradient(#d5d6d7,#e6e7e8);border:1px solid #f2f2f2;color:#555;font-size:14px;display:flex;align-items:center;padding-left:15px;white-space:nowrap}
.field.select::after{content:"";position:absolute;right:18px;top:15px;border:7px solid transparent;border-top:9px solid #9a9c9e}
.field.area{width:460px;height:140px;align-items:flex-start;padding:10px 15px;line-height:17px;white-space:normal}
.send{position:absolute;left:902px;top:208px;width:98px;height:40px;background:var(--navy);color:#fff;font-weight:600;font-size:14px;display:flex;align-items:center;justify-content:center;gap:10px}
.close{left:120px;top:682px;width:117px;height:23px;background:var(--navy);color:var(--lime);font-size:14px;display:flex;align-items:center;justify-content:center}

.section-title{font-size:21px;color:var(--lime);font-weight:400}
.testimonials{left:120px;top:794px;width:310px}
.testimonial{font-style:italic;font-weight:300;font-size:12px;line-height:14.5px;letter-spacing:-.1px;color:#c8d6e4}
.author{font-size:12px;line-height:15px;margin:12px 0 0}
.author strong{font-weight:600;display:block}
.testimonials .testimonial + .author + .testimonial{margin-top:42px}
.about{left:470px;top:792px;width:262px;font-size:12px;line-height:18px;letter-spacing:-.15px;font-weight:300;color:#dde6ef}
.about strong{font-weight:600;color:#fff}
.more{left:470px;top:1010px;width:120px;height:35px;background:var(--navy);font-size:12.5px;font-weight:600;display:flex;align-items:center;justify-content:center;gap:8px}
.card{position:absolute;left:790px;width:290px;height:65px;background:var(--navy);padding:13px 0 0 23px}
.card h3{font-size:16px;font-weight:400}
.card span{font-size:12px;color:var(--lime)}
.card.alt{background:var(--lime);color:var(--navy)}
.card.alt span{color:var(--navy)}
.card svg{position:absolute;right:20px;top:21px}

.footer{left:0;top:1110px;width:1200px;height:51px;background:#0a3258;border-top:1px solid #08294a}
.footer p{position:absolute;left:120px;top:18px;font-size:12.5px;color:#b9c8d8}
.footer strong{color:#fff;font-weight:500}
.footer-links{position:absolute;right:120px;top:18px;display:flex;align-items:center;gap:6px;font-size:12.5px;color:#b9c8d8}
.social{width:14px;height:14px;display:inline-block}
.footer-links u{color:#fff}
</style>
</head>
<body>

<header>
  <div class="abs logo"><span class="logo-mark"></span>TOVEN</div>
  <nav class="abs nav">
    <a class="current" href="#">HOME<i class="corner c-tr"></i><i class="corner c-bl"></i></a>
    <a href="#">ABOUT US</a><a href="#">OUR SERVICES</a><a href="#">TECHNOLOGY</a><a href="#">PORTFOLIO</a><a href="#" style="margin-right:0">CONTACT US</a>
  </nav>
  <div class="abs rule" style="left:80px;top:71px;width:1040px"></div>
</header>

<h1 class="abs headline"><span>WEB APPLICATION</span> DEVELOPMENT AND SUPPORT</h1>

<section class="abs hero">
  <div class="code-art" role="img" aria-label="Faded lines of source code fanning behind the monitor"></div>
  <h2>DO YOU WANT COMPLEX APPLICATION<br>THAT WILL WORK FOR YOU?</h2>
  <ul class="benefits">
    <li><svg width="14" height="12"><path d="M1 6l4 4 8-9" stroke="#a6bd2a" stroke-width="3" fill="none"/></svg>We can turn your <b>business processes into online web applications</b>.</li>
    <li><svg width="14" height="12"><path d="M1 6l4 4 8-9" stroke="#a6bd2a" stroke-width="3" fill="none"/></svg>We can get your <b>products or services selling online</b>.</li>
    <li><svg width="14" height="12"><path d="M1 6l4 4 8-9" stroke="#a6bd2a" stroke-width="3" fill="none"/></svg>We can convert your site into one that you can <b>maintain yourself</b>.</li>
    <li><svg width="14" height="12"><path d="M1 6l4 4 8-9" stroke="#a6bd2a" stroke-width="3" fill="none"/></svg>We can help ensure your website is <b>usable and standards compliant</b>.</li>
  </ul>
  <a class="pricing">
    <svg width="32" height="30" viewBox="0 0 32 30"><g fill="#fff"><ellipse cx="16" cy="24" rx="14" ry="5"/><ellipse cx="16" cy="17" rx="14" ry="5"/><ellipse cx="16" cy="10" rx="14" ry="5"/></g><g fill="none" stroke="#c9d63b" stroke-width="1.5"><ellipse cx="16" cy="17" rx="14" ry="5"/><ellipse cx="16" cy="10" rx="14" ry="5"/></g></svg>
    SEE PRICING
  </a>
</section>
<div class="abs monitor" role="img" aria-label="Desktop monitor showing the AurumVault website built by Toven"></div>

<section class="abs quote-panel">
  <p><b>FILL IN THIS FORM</b> AND WE’LL EMAIL YOU A <b>QUOTE</b> FOR YOUR REQUIREMENTS:</p>
  <div class="field" style="left:40px;top:58px">Your &nbsp;name</div>
  <div class="field" style="left:40px;top:108px">Your &nbsp;e-mail</div>
  <div class="field" style="left:40px;top:158px">Your phone number</div>
  <div class="field" style="left:40px;top:208px">Company name</div>
  <div class="field" style="left:290px;top:58px">Your current web address</div>
  <div class="field select" style="left:290px;top:108px">Service of interest</div>
  <div class="field select" style="left:290px;top:158px">Your budget</div>
  <div class="field select" style="left:290px;top:208px">How did you hear about us</div>
  <div class="field area" style="left:540px;top:58px">Enter as much additional information / description of your requirements into this box as you can..</div>
  <div class="send">Send! <svg width="12" height="12"><path d="M1 1l5 5-5 5M6 1l5 5-5 5" stroke="#fff" stroke-width="2" fill="none"/></svg></div>
</section>
<div class="abs close">CLOSE</div>

<h2 class="abs section-title" style="left:120px;top:742px">TESTIMONIALS</h2>
<div class="abs rule" style="left:80px;top:774px;width:360px"></div>
<h2 class="abs section-title" style="left:470px;top:742px">ABOUT US</h2>
<div class="abs rule" style="left:470px;top:774px;width:650px"></div>

<div class="abs testimonials">
  <blockquote class="testimonial">“Lorem ipsum dolor sit amet, consectetur adipiscing elit. Duis commodo, libero eu ultrices elementum, nisi turpis sagittis leo, ut lacinia enim velit pharetra neque. Nulla mollis dictum laoreet. Nam lectus mauris, vestibulum ut placerat sit amet, aliquet sed lacus.”</blockquote>
  <div class="author"><strong>PETER HALE</strong>Chairman, AurumVault</div>
  <blockquote class="testimonial">Phasellus tempus justo quis est congue aliquet. Integer arcu tortor, rhoncus eu facilisis consectetur, pulvinar nec tortor. Sed turpis enim, egestas vehicula laoreet quis.”</blockquote>
  <div class="author"><strong>NEIL CARVER</strong>Chairman, Lumaray</div>
</div>

<p class="abs about"><strong>Toven Limited</strong> was founded in March 2004 and is based at Harrowmede Court in Milton Keynes. The original purpose of the business was to develop websites for any industry. Since then, the company has continued to develop websites, but has specialised in online application systems. The company has also branched out into IT management and support services. The company is in a growth phase taking on projects of ever increasing complexity while still welcoming smaller projects.</p>
<a class="abs more">Find out more <svg width="12" height="12"><path d="M1 1l5 5-5 5M6 1l5 5-5 5" stroke="#fff" stroke-width="2" fill="none"/></svg><i class="corner c-tr"></i><i class="corner c-bl"></i></a>

<div class="card" style="top:796px"><h3>Our services</h3><span>What can we do for you?</span><svg width="22" height="22"><path d="M2 2l9 9-9 9M11 2l9 9-9 9" stroke="#fff" stroke-width="3" fill="none"/></svg><i class="corner c-tr"></i><i class="corner c-bl"></i></div>
<div class="card alt" style="top:876px"><h3>The technology</h3><span>What technologies do we use?</span><svg width="22" height="22"><path d="M2 2l9 9-9 9M11 2l9 9-9 9" stroke="#0b2744" stroke-width="3" fill="none"/></svg><i class="corner c-tr" style="border-color:var(--navy)"></i><i class="corner c-bl" style="border-color:var(--navy)"></i></div>
<div class="card" style="top:956px"><h3>Our work</h3><span>Some examples of our work.</span><svg width="22" height="22"><path d="M2 2l9 9-9 9M11 2l9 9-9 9" stroke="#fff" stroke-width="3" fill="none"/></svg><i class="corner c-tr"></i><i class="corner c-bl"></i></div>

<footer class="abs footer">
  <p>© <strong>Toven Ltd</strong>. 2012 Registered in England &amp; Wales Number: 04918372.</p>
  <div class="footer-links">
    <span class="social" style="background:#3b5b9a"></span>
    <span class="social" style="background:#3aa3db"></span>
    <span class="social" style="background:#e9762b"></span>
    <span>&nbsp;|&nbsp;</span><u>sitemap</u><span>&nbsp;|&nbsp;</span>login
  </div>
</footer>

</body>
</html>
```